Stationary - Business Card/Letterhead and envelope design

Details for my new Stationery Design Project will be added soon. , I have two logos I am trying to decide on. I will upload the eps logos shortly. I have attached a file of what i have so far. I need urgently Business cards, but also will need a letterhead template and envelopes.

PLEASE NOTE THE DEADLINE SAYS 2 DAYS but I need business card design in LESS THAN A DAY.

thanks, Details for my new Stationery Design Project will be added soon. , I have two logos I am trying to decide on. I will upload the eps logos shortly. I have attached a file of what i have so far. I need urgently Business cards, but also will need a letterhead template and envelopes.

thanks
Updates

I have uploaded one of the logos you can work with. hopefully the other one comes soon.

details for the business card.

Marla Thorne

Managing Director

P&K Ventures Ltd

Bda: 1-441-555-0193

Email: marla@pkvnbda.com

web: www.pkvnbda.com

Industry/Entity Type

Business

```html
<!DOCTYPE html>
<html lang="en">
<head>
<meta charset="utf-8">
<title>P&amp;K Ventures Ltd – Business Card</title>
<link rel="stylesheet" href="https://fonts.googleapis.com/css2?family=Russo+One&family=Roboto:wght@400&family=Ubuntu:wght@500&family=Abel&display=swap">
<style>
  :root {
    --backdrop: #c4d975;
    --card: #ffffff;
    --cyan: #16b4cc;
    --brown: #7c6a56;
    --ink: #111111;
  }
  * { margin: 0; padding: 0; box-sizing: border-box; }
  html, body { width: 1200px; height: 1076px; overflow: hidden; }
  body { background: var(--backdrop); position: relative; }

  .card {
    position: absolute;
    left: 256px;
    width: 650px;
    height: 350px;
    border-radius: 10px;
    overflow: hidden;
    background: var(--card);
    box-shadow: 0 1px 5px rgba(0,0,0,.35);
  }
  .card--front { top: 117px; }
  .card--back { top: 550px; }

  /* front */
  .front__band-cyan { position: absolute; left: 0; right: 0; top: 297px; height: 17px; background: var(--cyan); }
  .front__band-brown { position: absolute; left: 0; right: 0; top: 314px; bottom: 0; background: var(--brown); }

  .brand-name {
    position: absolute;
    font-family: "Russo One", sans-serif;
    color: var(--cyan);
    white-space: nowrap;
    line-height: 1;
  }
  .front__brand { left: 24px; top: 42px; font-size: 34px; }

  .web-address {
    position: absolute;
    font-family: "Russo One", sans-serif;
    font-size: 14px;
    letter-spacing: .3px;
    white-space: nowrap;
  }
  .front__web { right: 25px; top: 44px; color: var(--cyan); }

  .identity {
    position: absolute;
    right: 330px;
    top: 86px;
    text-align: right;
    color: var(--ink);
  }
  .identity__name { font-family: "Russo One", sans-serif; font-size: 29px; line-height: 36px; }
  .identity__role { font-family: "Russo One", sans-serif; font-size: 19px; line-height: 25px; }
  .identity__dept { font-family: "Russo One", sans-serif; font-size: 15px; line-height: 22px; }
  .identity__contact { font-family: "Roboto", sans-serif; font-size: 16px; line-height: 21px; }

  .front__divider {
    position: absolute;
    left: 345px;
    top: 141px;
    height: 144px;
    border-left: 2px dotted var(--ink);
  }

  .office {
    position: absolute;
    left: 376px;
    top: 140px;
    font-family: "Ubuntu", sans-serif;
    font-weight: 500;
    font-size: 16px;
    line-height: 22.5px;
    color: var(--ink);
  }

  /* back */
  .back__band-top { position: absolute; left: 0; right: 0; top: 0; height: 48px; background: var(--cyan); }
  .back__band-bottom { position: absolute; left: 0; right: 0; top: 185px; bottom: 0; background: var(--cyan); }
  .back__brand { left: 0; right: 0; top: 100px; font-size: 40px; text-align: center; }
  .back__tagline {
    position: absolute; left: 0; right: 0; top: 222px;
    text-align: center;
    font-family: "Abel", sans-serif;
    font-size: 23px;
    color: #ffffff;
    letter-spacing: .3px;
  }
  .back__web { left: 0; right: 0; top: 290px; text-align: center; color: #ffffff; }
</style>
</head>
<body>

  <section class="card card--front" aria-label="Business card front">
    <div class="brand-name front__brand">P&amp;K Ventures Ltd</div>
    <div class="web-address front__web">www.pkvnbda.com</div>

    <div class="identity">
      <div class="identity__name">MARLA THORNE</div>
      <div class="identity__role">ACCOUNT MANAGER</div>
      <div class="identity__dept">WEB DEVELOPMENT DEPARTEMENT</div>
      <div class="identity__contact">marla@pkvnbda.com</div>
      <div class="identity__contact">1-441-555-0193</div>
    </div>

    <div class="front__divider"></div>

    <address class="office" style="font-style:normal">
      Harbourline Digital Co<br>
      Cedar House 3rd floor,<br>
      14 Front Street Hamilton,<br>
      Bermuda HM 11<br>
      Telp. 1-441-555-0147 ext 13<br>
      Fax. 1-441-555-0148
    </address>

    <div class="front__band-cyan"></div>
    <div class="front__band-brown"></div>
  </section>

  <section class="card card--back" aria-label="Business card back">
    <div class="back__band-top"></div>
    <div class="brand-name back__brand">P&amp;K Ventures Ltd</div>
    <div class="back__band-bottom"></div>
    <p class="back__tagline">Corporate Analysis. Enhanced Responsibility</p>
    <div class="web-address back__web">www.pkvnbda.com</div>
  </section>

</body>
</html>
```